Corvatel Website Graphic design

we want a replacement of existing designs in our existing website.. we want you to suggest and create a better graphical designs which suits our service with good representation explaining our process and services
Website Url: https://corvatelq.example
Basic Requirements -
1. Flat architecture
2. A good color palette
3. Icons to support the Content
4. Consistent Images in alignment with the Business
5. Use white space to let the Content breathe

Target Market(s)

Manufacturers & E-Commerce Distributors

Industry/Entity Type

Data Service

Colors

Designer to choose colors to be used in the design.

Requirements
Must have
• Creativity and originality
Nice to have
• Try to keep it Simple

```html
<!DOCTYPE html>
<html lang="en">
<head>
<meta charset="utf-8">
<title>Corvatel Solutions</title>
<link href="https://fonts.googleapis.com/css2?family=Montserrat:wght@300;400;500;600;700&family=Arimo:wght@400;700&display=swap" rel="stylesheet">
<style>
  :root{
    --navy-900:#0a1330;
    --navy-800:#0e1a40;
    --navy-700:#13245a;
    --teal:#5fd4de;
    --teal-muted:#4a8f98;
    --slate-block:#3d5596;
    --white:#ffffff;
    --ink:#1a1a1a;
    --link-blue:#1f3d8e;
    --muted:#6c6f78;
  }
  *{margin:0;padding:0;box-sizing:border-box}
  html,body{width:1200px;height:4396px;overflow:hidden}
  body{position:relative;font-family:"Montserrat",sans-serif;color:var(--white);
    background:linear-gradient(180deg,var(--navy-800) 0,#10204e 1400px,var(--navy-900) 2594px,var(--white) 2594px)}
  .abs{position:absolute}

  /* nav */
  .brand{display:flex;align-items:center;gap:10px;color:var(--white);font-weight:500;font-size:17px;line-height:1.05}
  .brand-mark{width:28px;height:28px;border-radius:50%;background:var(--teal)}
  .site-nav{left:0;top:0;width:1200px;height:100px}
  .site-nav .brand{position:absolute;left:75px;top:33px}
  .nav-links{position:absolute;right:73px;top:43px;display:flex;gap:40px;font-size:14px;font-weight:500;letter-spacing:.3px}
  .nav-links a{color:var(--white);text-decoration:none;padding-bottom:8px}
  .nav-links a.active{border-bottom:1px solid var(--white)}

  /* hero */
  .hero-photo{left:0;top:0;width:1200px;height:700px;
    background:radial-gradient(ellipse at 55% 40%,#2a4a86 0,#1a2f63 35%,transparent 70%),
               linear-gradient(180deg,#13275e 0,#1b3671 45%,#16295a 75%,var(--navy-800) 100%)}
  .hero-title{left:75px;top:232px;font-size:62px;line-height:58px;letter-spacing:1px}
  .hero-title .light{font-weight:300;display:block}
  .hero-title .bold{font-weight:700;display:block}
  .hero-sub{left:76px;top:366px;font-size:15px;font-weight:400;color:#c8d2e6}
  .btn-outline{display:flex;align-items:center;justify-content:center;gap:14px;border:2px solid var(--teal);
    border-radius:26px;color:var(--white);font-weight:600;font-size:19px;text-decoration:none}
  .btn-about{left:76px;top:416px;width:174px;height:48px}

  /* value section */
  .eyebrow-teal{left:87px;top:793px;font-size:17px;font-weight:500;color:var(--teal)}
  .value-title{left:87px;top:815px;font-family:"Arimo",sans-serif;font-weight:700;font-size:38px}
  .value-text{left:87px;top:880px;width:640px;font-size:21px;line-height:27px;font-weight:400;color:#dfe5f1}
  .card-img{width:308px;height:204px;top:997px;border-radius:16px}
  .card-num{top:1237px;font-size:22px;font-weight:500;color:var(--teal)}
  .card-rule{top:1272px;width:218px;height:2px;background:#c9d1e2}
  .card-title{top:1285px;font-size:22px;line-height:27px;font-weight:600}
  .timeline{left:0;top:1433px;width:807px;height:2px;background:var(--teal)}
  .timeline-dot{left:800px;top:1427px;width:14px;height:14px;border-radius:50%;background:var(--teal)}
  .btn-services{left:872px;top:1410px;width:242px;height:50px}

  /* solutions */
  .solutions-title{left:87px;top:1638px;font-size:31px;font-weight:400;letter-spacing:.5px}
  .solutions-title b{font-weight:700}
  .accent-block{background:var(--slate-block)}
  .building-photo{left:599px;top:1640px;width:601px;height:442px;border-radius:6px 0 0 6px;
    background:linear-gradient(120deg,#6f93d6 0,#3f68b8 40%,#2a4f9e 70%,#5f86cc 100%)}
  .service{left:150px;display:flex;gap:24px;align-items:flex-start}
  .service svg{flex:none}
  .service h3{font-size:19px;font-weight:500;letter-spacing:.3px}
  .service p{font-size:19px;line-height:23px;color:#d3dbeb;font-weight:400}

  .years-num{left:82px;top:2178px;font-size:186px;font-weight:600;letter-spacing:-4px;line-height:1}
  .years-title{left:375px;top:2255px;font-size:49px;font-weight:600}
  .years-sub{left:375px;top:2313px;font-size:32px;font-weight:400;color:#d3dbeb}

  /* slider */
  .slider-photo{left:0;top:2601px;width:1200px;height:506px;
    background:linear-gradient(100deg,#1a3a6e 0,#2d5fa0 25%,#7b6a5a 55%,#a98f78 75%,#4e3f35 100%)}
  .slider-arrow{top:2828px}

  /* blogs */
  .eyebrow-dark{left:87px;top:3190px;font-size:17px;font-weight:500;color:var(--ink)}
  .blogs-title{left:87px;top:3210px;font-family:"Arimo",sans-serif;font-weight:700;font-size:38px;color:var(--ink)}
  .blog-img{top:3306px;width:308px;height:204px;border-radius:16px}
  .blog-meta{top:3522px;width:302px}
  .blog-meta h4{font-size:17px;font-weight:500;color:var(--link-blue)}
  .blog-meta time{display:block;font-size:12px;color:var(--muted);margin-top:2px}
  .blog-actions{position:absolute;right:0;top:1px;display:flex;gap:8px}
  .see-posts{left:952px;top:3620px;display:flex;align-items:center;gap:14px;font-size:19px;font-weight:500;color:var(--ink);text-decoration:none}

  /* footer */
  .site-footer{left:0;top:3737px;width:1200px;height:659px;background:linear-gradient(180deg,#0e1c4a 0,#0b1638 100%)}
  .cta-title{left:0;top:3888px;width:1200px;text-align:center;font-size:37px;font-weight:600}
  .cta-sub{left:0;top:3942px;width:1200px;text-align:center;font-size:18px;color:#d3dbeb}
  .field{top:3999px;height:37px;border:1.5px solid #c9d1e2;border-radius:19px;background:transparent;
    color:var(--white);font-family:"Montserrat",sans-serif;font-size:15px;padding:0 16px;display:flex;align-items:center}
  .btn-submit{left:857px;top:4000px;width:117px;height:36px;border-radius:18px;background:var(--teal-muted);
    color:var(--white);font-size:13px;font-weight:600;display:flex;align-items:center;justify-content:center;letter-spacing:.5px}
  .site-footer-brand{left:535px;top:4185px}
  .contact-row{left:411px;top:4244px;width:376px;display:flex;justify-content:space-between;font-size:12px;color:#d3dbeb}
  .contact-row span{display:flex;align-items:center;gap:6px}
  .contact-rule{left:411px;top:4277px;width:376px;height:1px;background:#7d88a6}
  .copyright{left:0;top:4296px;width:1200px;text-align:center;font-size:9px;color:#b3bdd3;letter-spacing:.3px}
</style>
</head>
<body>

<div class="abs hero-photo" role="img" aria-label="Night city skyline beneath a glowing data network"></div>

<header class="abs site-nav">
  <div class="brand"><span class="brand-mark"></span><span>Corvatel<br>Solutions</span></div>
  <nav class="nav-links">
    <a class="active" href="#">HOME</a><a href="#">ABOUT</a><a href="#">SERVICES</a><a href="#">CONTACT US</a>
  </nav>
</header>

<h1 class="abs hero-title"><span class="light">Nothing works better</span><span class="bold">than a solution.</span></h1>
<p class="abs hero-sub">Solutions to Extract, Analyse, Clean up, Validate and Enrich your data</p>
<a class="abs btn-outline btn-about" href="#">About us
  <svg width="22" height="22" viewBox="0 0 22 22"><circle cx="11" cy="11" r="9" fill="none" stroke="#fff" stroke-width="2"/><path d="M6.5 11h8M11 7.5l3.5 3.5-3.5 3.5" fill="none" stroke="#fff" stroke-width="2"/></svg></a>

<p class="abs eyebrow-teal">BETTER DATA, BETTER DECISIONS,</p>
<h2 class="abs value-title">Better ROI.</h2>
<p class="abs value-text">Our value added services help companies realize the full potential of ERP and e-Commerce implementations.</p>

<div class="abs card-img" style="left:89px;background:linear-gradient(160deg,#e8e6e2,#a39a8f 60%,#5a4a3c)" role="img" aria-label="Empty conference room with chairs around a long table"></div>
<div class="abs card-img" style="left:447px;background:linear-gradient(150deg,#d9dde4,#8d97a8 50%,#3a3f48)" role="img" aria-label="Hand holding a payment card beside a laptop"></div>
<div class="abs card-img" style="left:806px;background:linear-gradient(150deg,#5b4636,#c9c3bb 50%,#3e3128)" role="img" aria-label="Team fist bump over a desk with devices and papers"></div>

<div class="abs card-num" style="left:87px">01</div><div class="abs card-rule" style="left:87px"></div>
<div class="abs card-title" style="left:87px">MASTER DATA<br>MANAGEMENT</div>
<div class="abs card-num" style="left:445px">01</div><div class="abs card-rule" style="left:445px"></div>
<div class="abs card-title" style="left:445px">MASTER DATA<br>MANAGEMENT</div>
<div class="abs card-num" style="left:803px">01</div><div class="abs card-rule" style="left:803px"></div>
<div class="abs card-title" style="left:803px">MASTER DATA<br>MANAGEMENT</div>

<div class="abs timeline"></div><div class="abs timeline-dot"></div>
<a class="abs btn-outline btn-services" href="#">See all services
  <svg width="22" height="22" viewBox="0 0 22 22"><circle cx="11" cy="11" r="9" fill="none" stroke="#fff" stroke-width="2"/><path d="M6.5 11h8M11 7.5l3.5 3.5-3.5 3.5" fill="none" stroke="#fff" stroke-width="2"/></svg></a>

<h2 class="abs solutions-title">WE SHOW YOU <b>SOLUTIONS.</b></h2>
<div class="abs accent-block" style="left:681px;top:1584px;width:89px;height:60px"></div>
<div class="abs building-photo" role="img" aria-label="Glass office towers seen from below"></div>
<div class="abs accent-block" style="left:1024px;top:1988px;width:116px;height:362px;opacity:.92"></div>

<div class="abs service" style="top:1734px">
  <svg width="62" height="66" viewBox="0 0 62 66"><g fill="none" stroke="#cfe9ef" stroke-width="3"><ellipse cx="31" cy="10" rx="27" ry="8"/><path d="M4 10v46c0 4.5 12 8 27 8s27-3.5 27-8V10"/><path d="M4 33c0 4.5 12 8 27 8s27-3.5 27-8"/></g></svg>
  <div><h3>SERVICE1</h3><p>Enter your short description<br>right here.</p></div>
</div>
<div class="abs service" style="top:1860px">
  <svg width="62" height="66" viewBox="0 0 62 66"><rect x="4" y="2" width="54" height="5" fill="#cfe9ef"/><path d="M31 14 10 36h14v26h14V36h14z" fill="#cfe9ef"/></svg>
  <div><h3>SERVICE2</h3><p>Enter your short description<br>right here.</p></div>
</div>
<div class="abs service" style="top:1986px">
  <svg width="62" height="66" viewBox="0 0 62 66"><circle cx="31" cy="34" r="23" fill="none" stroke="#7fd0d6" stroke-width="8" stroke-dasharray="120 10 10 10"/></svg>
  <div><h3>SERVICE3</h3><p>Enter your short description<br>right here.</p></div>
</div>

<div class="abs years-num">20</div>
<div class="abs years-title">YEARS OF EXPERIENCE</div>
<div class="abs years-sub">Short line here.</div>

<div class="abs slider-photo" role="img" aria-label="Hands typing code on a laptop beside a coffee mug"></div>
<svg class="abs slider-arrow" style="left:30px" width="20" height="36" viewBox="0 0 20 36"><path d="M17 3 3 18l14 15" fill="none" stroke="#111" stroke-width="4"/></svg>
<svg class="abs slider-arrow" style="left:1152px" width="20" height="36" viewBox="0 0 20 36"><path d="M3 3l14 15L3 33" fill="none" stroke="#111" stroke-width="4"/></svg>

<p class="abs eyebrow-dark">KNOW MORE ABOUT US</p>
<h2 class="abs blogs-title">Read our latest blogs.</h2>

<div class="abs blog-img" style="left:89px;background:linear-gradient(150deg,#b8b8b4,#e8e8e6 50%,#6b6d70)" role="img" aria-label="Person using a tablet at a desk with coffee"></div>
<div class="abs blog-img" style="left:447px;background:linear-gradient(150deg,#2f2f35,#6d6a74 50%,#26262b)" role="img" aria-label="Close-up of app icons on a phone screen"></div>
<div class="abs blog-img" style="left:806px;background:linear-gradient(150deg,#0d3c5a,#1f7ea3 50%,#0b2f48)" role="img" aria-label="Blue glowing web publishing screen"></div>

<div class="abs blog-meta" style="left:92px"><h4>BLOG TITLE HERE</h4><time>January 9, 2020</time>
  <div class="blog-actions"><svg width="18" height="16" viewBox="0 0 18 16"><path d="M9 15 2 8a4 4 0 0 1 7-5 4 4 0 0 1 7 5z" fill="#1f3d8e"/></svg><svg width="16" height="16" viewBox="0 0 16 16"><path d="M9 2l6 5-6 5V9C5 9 3 10 1 14c0-5 3-8 8-8z" fill="#1f3d8e"/></svg></div></div>
<div class="abs blog-meta" style="left:450px"><h4>BLOG TITLE HERE</h4><time>January 9, 2020</time>
  <div class="blog-actions"><svg width="18" height="16" viewBox="0 0 18 16"><path d="M9 15 2 8a4 4 0 0 1 7-5 4 4 0 0 1 7 5z" fill="#1f3d8e"/></svg><svg width="16" height="16" viewBox="0 0 16 16"><path d="M9 2l6 5-6 5V9C5 9 3 10 1 14c0-5 3-8 8-8z" fill="#1f3d8e"/></svg></div></div>
<div class="abs blog-meta" style="left:809px"><h4>BLOG TITLE HERE</h4><time>January 9, 2020</time>
  <div class="blog-actions"><svg width="18" height="16" viewBox="0 0 18 16"><path d="M9 15 2 8a4 4 0 0 1 7-5 4 4 0 0 1 7 5z" fill="#1f3d8e"/></svg><svg width="16" height="16" viewBox="0 0 16 16"><path d="M9 2l6 5-6 5V9C5 9 3 10 1 14c0-5 3-8 8-8z" fill="#1f3d8e"/></svg></div></div>

<a class="abs see-posts" href="#">See all posts
  <svg width="22" height="22" viewBox="0 0 22 22"><circle cx="11" cy="11" r="9" fill="none" stroke="#1a1a1a" stroke-width="2"/><path d="M6.5 11h8M11 7.5l3.5 3.5-3.5 3.5" fill="none" stroke="#1a1a1a" stroke-width="2"/></svg></a>

<footer class="abs site-footer"></footer>
<h2 class="abs cta-title">Request for a sample data</h2>
<p class="abs cta-sub">Try our service</p>
<div class="abs field" style="left:227px;width:296px">Full Name...</div>
<div class="abs field" style="left:541px;width:298px">Email address...</div>
<div class="abs btn-submit">SUBMIT</div>

<div class="abs brand site-footer-brand"><span class="brand-mark"></span><span>Corvatel<br>Solutions</span></div>
<div class="abs contact-row">
  <span><svg width="13" height="10" viewBox="0 0 13 10"><rect x=".5" y=".5" width="12" height="9" fill="none" stroke="#d3dbeb"/><path d="M.5 .5 6.5 5l6-4.5" fill="none" stroke="#d3dbeb"/></svg>hello@corvatelq.example</span>
  <span><svg width="12" height="12" viewBox="0 0 12 12"><path d="M2 1l2.5 0 1 3-1.5 1a7 7 0 0 0 3 3l1-1.5 3 1V10c0 1-1 1.5-2 1.3C5 10.5 1.5 7 .7 3 .5 2 1 1 2 1z" fill="none" stroke="#d3dbeb"/></svg>(02) 555 0148</span>
  <span><svg width="12" height="12" viewBox="0 0 12 12"><path d="M2 1l2.5 0 1 3-1.5 1a7 7 0 0 0 3 3l1-1.5 3 1V10c0 1-1 1.5-2 1.3C5 10.5 1.5 7 .7 3 .5 2 1 1 2 1z" fill="none" stroke="#d3dbeb"/></svg>(02) 555 0148</span>
</div>
<div class="abs contact-rule"></div>
<p class="abs copyright">©2020 Corvatel Solutions | ALL RIGHTS RESERVED</p>

</body>
</html>
```